Post Disaster Temporary Housing Literature Review poster

Wanting a poster design for two Emergency Management conferences we have coming up. The information to be included in the poster is capturing the purpose, findings and recommendations from a post disaster temporary housing literature review looking at “What should government consider in order to improve planning and decision making for accommodation needs after a disaster, and to support people’s transition to stable housing?”
I’d like to enhance the visual appeal through including relevant images or graphic. I am also open to reducing the text if needed.
The government group I work with focuses on the social and human side of disaster recovery so keen for any images to reflect the human aspect and not focus solely on disasters or housing.
Government and NGO's

```html
<!DOCTYPE html>
<html lang="en">
<head>
<meta charset="UTF-8">
<title>Post Disaster Temporary Housing Conference</title>
<link rel="stylesheet" href="https://fonts.googleapis.com/css2?family=Montserrat:wght@600;700&family=Lato:wght@400;700&display=swap">
<style>
  :root{
    --navy:#06202b;
    --teal:#0f6c80;
    --green-deep:#0b5a2c;
    --green:#077a27;
    --green-soft:#3a8f48;
    --white:#ffffff;
    --text:#f2f6f7;
    --rule:rgba(255,255,255,.55);
  }
  *{margin:0;padding:0;box-sizing:border-box}
  html,body{width:848px;height:1200px;overflow:hidden;background:#ffffff}
  .poster{
    position:relative;width:848px;height:1200px;overflow:hidden;
    background:linear-gradient(160deg,var(--navy) 0%,#082a36 45%,#0b4a5c 75%,var(--teal) 100%);
    font-family:'Lato',sans-serif;color:var(--text);
  }
  .art{position:absolute;left:0;top:0;width:848px;height:760px}
  .title{
    position:absolute;left:41px;top:28px;
    font-family:'Montserrat',sans-serif;font-weight:700;font-size:30px;line-height:45px;color:var(--white);
    text-shadow:0 2px 6px rgba(0,0,0,.35);
  }
  .question{
    position:absolute;left:43px;top:128px;width:390px;
    font-weight:700;font-size:18px;line-height:40px;color:var(--white);
    text-shadow:0 1px 4px rgba(0,0,0,.35);
  }
  .org{
    position:absolute;left:218px;top:336px;width:148px;height:148px;border-radius:50%;
    background:var(--white);display:flex;flex-direction:column;align-items:center;justify-content:center;
    color:#1d2a30;font-family:'Lato',sans-serif;font-weight:400;font-size:11.5px;line-height:19px;text-align:center;
  }
  .org-dot{width:40px;height:40px;border-radius:50%;border:2px solid #4aa8c8;margin-bottom:10px}
  h2{font-family:'Montserrat',sans-serif;font-weight:700;color:var(--white)}
  .purpose h2{position:absolute;left:43px;top:768px;font-size:26px}
  .purpose p{position:absolute;left:42px;top:815px;width:345px;font-size:15px;line-height:31.5px;text-align:justify;text-align-last:left}
  .findings h2{position:absolute;left:40px;top:992px;font-size:26px}
  .findings ol{position:absolute;left:42px;top:1038px;width:340px;list-style:none;font-size:15px;line-height:31px}
  .findings li{margin-bottom:5px}
  .divider{position:absolute;left:421px;top:766px;width:1px;height:408px;background:var(--rule)}
  .recs h2{position:absolute;left:458px;top:762px;font-size:26.5px}
  .recs ol{position:absolute;top:806px;list-style:none;font-size:15.5px;line-height:34.5px}
  .recs .col-a{left:459px}
  .recs .col-b{left:619px}
  .next h2{position:absolute;left:458px;top:994px;font-size:26px}
  .next p{position:absolute;left:461px;top:1036px;width:360px;font-size:13.5px;line-height:25.6px}
  .email{position:absolute;left:460px;top:1148px;display:flex;align-items:center;gap:7px;font-size:15.5px;font-weight:700;color:var(--white)}
  .email span{text-decoration:underline}
  .code{position:absolute;right:8px;top:1164px;font-family:'Montserrat',sans-serif;font-weight:700;font-size:12px;color:var(--white)}
  .band{position:absolute;left:0;bottom:0;width:848px;height:12px;background:#1c8a2c}
</style>
</head>
<body>
<div class="poster">
  <svg class="art" viewBox="0 0 848 760" xmlns="http://www.w3.org/2000/svg">
    <defs>
      <linearGradient id="houseTones" x1="0" y1="0" x2="1" y2="1">
        <stop offset="0" stop-color="#c9b58f"/>
        <stop offset=".5" stop-color="#a07a52"/>
        <stop offset="1" stop-color="#6e5238"/>
      </linearGradient>
      <linearGradient id="coupleTones" x1="0" y1="0" x2="0" y2="1">
        <stop offset="0" stop-color="#9aa58c"/>
        <stop offset=".55" stop-color="#6e6650"/>
        <stop offset="1" stop-color="#5d7a3c"/>
      </linearGradient>
      <linearGradient id="workerTones" x1="0" y1="0" x2="0" y2="1">
        <stop offset="0" stop-color="#b7c4cf"/>
        <stop offset=".5" stop-color="#9c7a55"/>
        <stop offset="1" stop-color="#5a4736"/>
      </linearGradient>
      <clipPath id="houseClip"><circle cx="620" cy="-60" r="627"/></clipPath>
    </defs>
    <circle cx="620" cy="-60" r="790" fill="var(--green-deep)" opacity=".85"/>
    <circle cx="620" cy="-60" r="710" fill="var(--green)"/>
    <rect x="0" y="0" width="848" height="760" clip-path="url(#houseClip)" fill="url(#houseTones)" role="img" aria-label="Photo of a storm-damaged brick and timber house with debris in the yard"/>
    <circle cx="300" cy="118" r="178" fill="var(--green-soft)" opacity=".9"/>
    <circle cx="100" cy="548" r="190" fill="url(#coupleTones)" stroke="#ffffff" stroke-width="1.5" role="img" aria-label="Photo of an older couple seen from behind looking at their damaged home"/>
    <path d="M-90 548 A190 190 0 0 1 290 548 Z" fill="none"/>
    <ellipse cx="130" cy="370" rx="110" ry="32" fill="var(--green)" opacity=".9"/>
    <circle cx="292" cy="410" r="88" fill="#ffffff" opacity=".12"/>
    <circle cx="328" cy="700" r="50" fill="url(#workerTones)" stroke="#ffffff" stroke-width="1.5" role="img" aria-label="Photo of two recovery workers surveying a destroyed neighbourhood"/>
  </svg>

  <h1 class="title">Post Disaster Temporary<br>Housing Conference</h1>
  <p class="question">What should government consider in order to improve planning and decision making for accommodation needs after a disaster, and to support people’s transition to stable housing?</p>

  <div class="org">
    <div class="org-dot"></div>
    Community Recovery<br>Reference Forum<br>AUSTRALIA
  </div>

  <section class="purpose">
    <h2>Purpose</h2>
    <p>There are currently significant challenges in supporting displaced people with timely and equitable access to emergency and temporary accommodation and assisting them on a path to stable housing in the aftermath of a disaster.</p>
  </section>

  <section class="findings">
    <h2>Findings</h2>
    <ol>
      <li>1. Leading practice in disaster housing recovery</li>
      <li>2. Innovative approaches to temporary housing</li>
      <li>3. A decision-making framework for resilient housing recovery</li>
    </ol>
  </section>

  <div class="divider"></div>

  <section class="recs">
    <h2>Recommendations</h2>
    <ol class="col-a">
      <li>1. Terminology</li>
      <li>2. Principles</li>
      <li>3. National Principles</li>
      <li>4. Guidelines</li>
      <li>5. Terminology</li>
    </ol>
    <ol class="col-b">
      <li>6. Funding</li>
      <li>7. Further Research</li>
      <li>8. Pilot Project</li>
      <li>9. Decision Making Framework</li>
      <li>10. Capturing Learnings</li>
    </ol>
  </section>

  <section class="next">
    <h2>Next Steps</h2>
    <p>The Community Recovery Reference Forum is partnering with Hazard Resilience Research Institute to analyse previous post-disaster temporary housing assistance and support mechanisms used in Australia</p>
  </section>

  <div class="email">
    <svg width="13" height="10" viewBox="0 0 13 10" aria-hidden="true"><rect x="0" y="0" width="13" height="10" rx="1" fill="#ffffff"/><path d="M0.5 0.8 L6.5 5.5 L12.5 0.8" fill="none" stroke="#0b3a48" stroke-width="1.3"/></svg>
    <span>alex.morgan@recoveryforum.org.au</span>
  </div>

  <div class="code">C52</div>
  <div class="band"></div>
</div>
</body>
</html>
```